price list for web and print- sending to inquiring clients and use as promo material

Hello
I need a graphic design for my photography price list/s. I am a people photographer. The first of 6 price sheets will be for head shots- I would like a price sheet that captures the prospective clients' attention. The info and visual should be compelling and easy to digest. It should be simple yet interesting. I will provide you with some pictures but you do not have to include them. I have a studio indoors and outdoors also working on location. This design should be for email and print. The picture of "ingrid" is me and I use that on all my profiles. I like the fonts in the logo but it is too boxy and rigid

Target Market(s)

repeat client, word of mouth referrals, new people but aquaintances of others that might know me

Industry/Entity Type

Graphic Design

Font styles to use
Serif
Sans Serif
Script

Requirements
Must have
• prices and maybe some words about my services that I sent in... Please tie it together as best as possible..
Nice to have
• Loosen up my logo.. it is in a box.....contemporary design but not something that would not fit in with corporate.. I like this headline
• "Create a great first impression with your professional headshots"
• I sent in other copy and my logo(sent in the picture drop box)

```html
<!DOCTYPE html>
<html lang="en">
<head>
<meta charset="utf-8">
<title>Ingrid M Harlow Photography – Headshot Price List</title>
<link href="https://fonts.googleapis.com/css2?family=Lato:wght@300;400;700&family=Lora:ital@1&display=swap" rel="stylesheet">
<style>
  :root {
    --page: #ffffff;
    --black: #000000;
    --ink-brown: #371b1b;
    --gold: #f2c98a;
    --tan: #b98a5c;
    --cream: #f6d9a8;
    --red: #a8292b;
    --red-deep: #8c2226;
    --maroon: #5b1b1d;
    --maroon-dark: #4a1a1b;
    --footer: #2f1a1a;
    --pink-text: #f2a395;
    --white: #ffffff;
  }
  * { margin: 0; padding: 0; box-sizing: border-box; }
  html, body { width: 771px; height: 1200px; overflow: hidden; background: var(--page); }
  body { position: relative; font-family: "Lato", sans-serif; }

  .sheet { position: absolute; left: 100px; top: 105px; width: 572px; height: 988px; background: var(--ink-brown); }

  .masthead { position: absolute; left: 0; top: 0; width: 572px; height: 153px; background: var(--black); }
  .brand { position: absolute; left: 0; top: 28px; width: 290px; text-align: center; color: var(--white); }
  .brand-dba { font-size: 13px; font-weight: 400; letter-spacing: 0.5px; }
  .brand-name { font-size: 30px; font-weight: 400; line-height: 1.15; margin-top: 8px; }
  .brand-name span { display: block; font-size: 17px; letter-spacing: 5px; margin-top: 6px; }
  .headline { position: absolute; left: 300px; top: 22px; font-family: "Lora", serif; font-style: italic; font-size: 22px; line-height: 25px; color: var(--gold); letter-spacing: 0.5px; }

  .collage { position: absolute; left: 0; top: 153px; width: 287px; height: 360px;
    background: linear-gradient(135deg, #3b2222 0%, #8a2b2b 35%, #a7a3a0 55%, #6e2323 75%, #2e1a1a 100%); }

  .highlights { position: absolute; left: 298px; top: 163px; width: 270px; }
  .highlight h2 { font-size: 18px; font-weight: 400; color: var(--cream); margin-bottom: 2px; }
  .highlight p { font-size: 14px; line-height: 18px; color: var(--tan); margin-bottom: 10px; }

  .packages-band { position: absolute; left: 0; top: 513px; width: 572px; height: 47px; background: var(--black);
    text-align: center; font-size: 30px; line-height: 47px; color: var(--cream); font-weight: 300; }
  .packages-band strong { font-weight: 700; color: var(--gold); }

  .package { position: absolute; padding: 18px 0 0 23px; color: var(--pink-text); font-size: 14px; line-height: 18px; }
  .package h3 { font-size: 14px; font-weight: 400; text-decoration: underline; text-underline-offset: 2px; }
  .entry { left: 0; top: 560px; width: 287px; height: 162px; background: var(--red); }
  .two-pose { left: 287px; top: 560px; width: 285px; height: 162px; background: var(--red-deep); padding-top: 10px; padding-left: 12px; }
  .premier { left: 0; top: 722px; width: 287px; height: 209px; background: var(--maroon); }
  .on-location { left: 287px; top: 722px; width: 285px; height: 209px; background: var(--maroon-dark); padding-top: 12px; padding-left: 12px; }
  .on-location h3 { letter-spacing: 5.5px; font-size: 15px; margin-bottom: 6px; }

  .contact { position: absolute; left: 0; top: 931px; width: 572px; height: 57px; background: var(--footer);
    color: var(--white); text-align: center; font-size: 13px; line-height: 17px; padding-top: 11px; }
</style>
</head>
<body>
<main class="sheet">
  <header class="masthead">
    <div class="brand">
      <p class="brand-dba">IMH PHOTO INC dba</p>
      <p class="brand-name">Ingrid M Harlow<span>PHOTOGRAPHY</span></p>
    </div>
    <h1 class="headline">Create a great<br>first impression<br>with your<br>professional headshots</h1>
  </header>

  <div class="collage" role="img" aria-label="Diamond collage of professional headshot portraits of smiling clients in business attire"></div>

  <section class="highlights">
    <div class="highlight">
      <h2>Experience</h2>
      <p>Ingrid is an accomplished professional photographer who has helped thousands of clients. She is an expert at helping you look confident and approchable</p>
    </div>
    <div class="highlight">
      <h2>24 Hour Turnaround</h2>
      <p>Your time is valuable. Ingrid can complete the photoshoot<br>in just 30 minutes.<br>(Or as long as you want.) Our process is designed to save your time.</p>
    </div>
    <div class="highlight">
      <h2>Enjoyable</h2>
      <p>You can look forward to an enjoyable photo session with Ingrid's professional guidence. Ingrid helps make the experience fun.</p>
    </div>
  </section>

  <div class="packages-band"><strong>Popular</strong> packages</div>

  <section class="package entry">
    <h3>ENTRY PACKAGE</h3>
    <p>Quick and Simple<br>- one pose<br>- one wardrobe<br>- one selected image retouched<br>- just $175<br>- Additional images just $75 each</p>
  </section>
  <section class="package two-pose">
    <h3>2 POSE PACKAGE</h3>
    <p>Most Popular<br>- two poses<br>- Two wardrobe changes<br>- Two selected images retouched<br>- One or two background changes<br>- just $175<br>- Additional images just $75 each</p>
  </section>
  <section class="package premier">
    <h3>PREMIER PACKAGE</h3>
    <p>Get it all | Most Popular<br>- four poses<br>- 3-4 wardrobe changes<br>- 4 selected images retouched<br>- 2-3 background changes<br>- Additional images just $75 each<br>- optional outdoor studio<br>-Just $525<br>Additional images just $75 each</p>
  </section>
  <section class="package on-location">
    <h3>At your location</h3>
    <p>$250 set up charge, minimum of 5 people one selected image retouched each additional image $50 each<br>If possible, we like ½ hour appts for each person so they can view their images on the computer<br>5-10 people $150 EACH<br>11-20 people $100 each<br>20+ $75 each</p>
  </section>

  <footer class="contact">
    4120 Linden Crest Parkway • Atlanta GA 30305 • 404-555-0147 cell 404-555-0192<br>
    imhphoto@lumenmail.com • http://imhphoto.com
  </footer>
</main>
</body>
</html>
```